Create a business Card for a Women Owned Business Body Positive Company. The winner we hope to work with on other projects coming up for grand opening for flyers, postcards, email marketing, facebook page, stationary, labels, tshirt design....
We would like if possible in the background of the card a infinity symbol or crown if it fits into the design if not it's ok. But I am open to all suggestions we had alot problems with the our new logo being created this time sad to say :(

Our colors are Royal Purple, Grey, Black Thank you in advance for your talent, you hard work and your submissions!
Delia and Nadine :)
Updates

my Logo is velvet harbor boutique which is purple and has a heart and infinity sign in it and my colors are purple silver and black only of another card i had done nothing else. My logo is VELVET HARBOR BOUTIQUE LOGO

Industry/Entity Type

Retail

Contact Information for Business Card

website: www.velvtharborboutiques.example email: sales@velvetharborboutique.example
Delia Pruett & Nadine Kolb Owners

Font styles to use
Script

Colors
b768aa

Requirements
Must have
• COLORS ARE PURPLE BLACK AND GREY
Nice to have
• INFINITY SIGNING IN THE BACKGROUND

```html
<!DOCTYPE html>
<html lang="en">
<head>
<meta charset="UTF-8">
<title>Velvet Harbor Boutique – Business Card</title>
<link href="https://fonts.googleapis.com/css2?family=Lato:wght@400;700&display=swap" rel="stylesheet">
<style>
  :root {
    --stage: #3a3a3a;
    --purple: #7a4597;
    --black: #0d0d0d;
    --ink: #1a1a1a;
    --white: #ffffff;
    --grey: #cfcfcf;
    --card-dark: #2b2b2b;
  }
  * { box-sizing: border-box; margin: 0; padding: 0; }
  html, body { width: 1200px; height: 900px; overflow: hidden; }
  body {
    background: var(--stage);
    font-family: "Lato", sans-serif;
    position: relative;
  }
  .card {
    position: absolute;
    width: 560px;
    height: 320px;
    border-radius: 4px;
    box-shadow: 0 18px 40px rgba(0,0,0,.45);
    overflow: hidden;
  }
  /* Front */
  .card--front { left: 70px; top: 500px; background: var(--white); }
  .card__swoosh { position: absolute; inset: 0; width: 100%; height: 100%; }
  .brand {
    position: absolute;
    color: var(--purple);
    font-weight: 400;
    text-align: center;
    letter-spacing: 2px;
    line-height: 1.15;
  }
  .card--front .brand { left: 210px; top: 30px; width: 300px; font-size: 26px; }
  .contact {
    position: absolute;
    left: 26px; top: 40px;
    list-style: none;
    font-size: 13px;
    color: var(--ink);
  }
  .contact li { display: flex; align-items: center; gap: 8px; height: 19px; }
  .contact svg { width: 11px; height: 11px; fill: var(--purple); flex: none; }
  .owners {
    position: absolute;
    right: 34px; top: 148px;
    text-align: left;
    color: var(--purple);
    font-weight: 700;
    font-size: 19px;
    line-height: 1.2;
  }
  .owners__role { color: var(--ink); font-weight: 400; font-size: 16px; padding-left: 44px; }
  .address {
    position: absolute;
    right: 60px; bottom: 40px;
    font-size: 16px;
    color: var(--ink);
    line-height: 1.25;
  }
  /* Back */
  .card--back {
    left: 570px; top: 110px;
    background: radial-gradient(ellipse at 40% 30%, #4a4a4a 0%, var(--card-dark) 55%, #171717 100%);
  }
  .card--back .brand { left: 80px; top: 100px; width: 400px; font-size: 32px; }
  .card--back .web {
    position: absolute;
    left: 0; width: 100%; top: 200px;
    text-align: center;
    color: var(--grey);
    font-size: 15px;
    letter-spacing: .5px;
  }
</style>
</head>
<body>

<section class="card card--front" aria-label="Business card front">
  <svg class="card__swoosh" viewBox="0 0 560 320" preserveAspectRatio="none" aria-hidden="true">
    <path d="M0 40 C 60 190, 260 300, 560 300 L560 320 L0 320 Z" fill="var(--purple)"/>
    <path d="M0 40 C 40 150, 150 250, 330 320 L300 320 C 140 260, 30 170, 0 90 Z" fill="var(--black)"/>
    <path d="M0 90 C 40 190, 170 280, 320 320 L0 320 Z" fill="var(--purple)"/>
  </svg>

  <div class="brand">VELVET HARBOR<br>BOUTIQUE</div>

  <ul class="contact">
    <li><svg viewBox="0 0 12 12"><path d="M2.5 1 L4.5 1 L5 3.5 L3.8 4.4 C4.4 5.8 5.6 7 7 7.6 L7.9 6.4 L10.5 7 L10.5 9 C10.5 10 9.7 10.7 8.7 10.6 C4.6 10.2 1.3 6.9 1 2.8 C0.9 1.8 1.5 1 2.5 1 Z"/></svg>555 014 2800</li>
    <li><svg viewBox="0 0 12 12"><rect x="3" y="0.5" width="6" height="11" rx="1"/><rect x="4" y="2" width="4" height="7" fill="#fff"/></svg>555 014 2801</li>
    <li><svg viewBox="0 0 12 12"><rect x="0.5" y="2" width="11" height="8" rx="1"/><path d="M1 2.5 L6 6.5 L11 2.5" stroke="#fff" fill="none"/></svg>sales@velvetharborboutique.example</li>
    <li><svg viewBox="0 0 12 12"><circle cx="6" cy="6" r="5.5"/><path d="M0.5 6 H11.5 M6 0.5 V11.5 M2 3 H10 M2 9 H10" stroke="#fff" stroke-width=".8" fill="none"/></svg>www.velvtharborboutiques.example</li>
  </ul>

  <div class="owners">
    Delia Pruett &amp;<br>Nadine Kolb
    <div class="owners__role">Owners</div>
  </div>

  <div class="address">418 Larkspur Row<br>Fairview, TX 75069</div>
</section>

<section class="card card--back" aria-label="Business card back">
  <div class="brand">VELVET HARBOR<br>BOUTIQUE</div>
  <div class="web">www.velvtharborboutiques.example</div>
</section>

</body>
</html>
```